UI Redesign For Mobile Events iPhone App

We need a new UI design for our Social Events mobile app. Our app called Vrenn is geared to help users find trending events in their local area. We show visual metrics on percent full and male female ratio and age group ratings. We want people to see whats going on at event before they get there through our app. Also we have a group chat portion to our app that we need included in the design. We would like to see a fresh, clean, and easy to use user interface that uses colors like, purple, blue and or hot pink.You may visit our website myvrenn.example for more information about what our app is geared to do.
Updates

Target Market(s)

Our target market people that use social networks and attend social events ranging from ages 16-44.

Industry/Entity Type

Events

Requirements
Must have
• We would like to see an Example layout of all screens. (UPDATE: Please use our current background in your design, A PSD has been uploaded for you to grab the background. The Vrenn Logo is NOT required to be included at the top of every screen)

-Profile Screen: Shows points earned, events attending, events created
-Event Listings Screen: Must have large image for event, visual metrics, date& time, location, attend button, invite friends button, Label for user who created the event
-Event Description Page: Shows everything as the event listing, has a description of the event, shows friends that are attending, points available
-Group Messaging Screen
-Slide Out Navigation Screen
-Notification Screen
-Ticket Screen
-Friends Activity Screen
-Friends Profile View: Shows events they've attended and points they've earned under their contact picture; invite button
-Sign-In Screen
-Register Screen

A way to label/categorize our different types of events:
-Nightlife
-Family
-Live Music & Concerts
-Restaurants
Group Chat Layout
Visual Meters for Percent Full, Male Female Ratio, Age Rating

```html
<!DOCTYPE html>
<html lang="en">
<head>
<meta charset="utf-8">
<title>My Vrenn Screen</title>
<link href="https://fonts.googleapis.com/css2?family=Roboto:wght@300;400;500&display=swap" rel="stylesheet">
<style>
  :root{
    --page-bg:#efe6e8;
    --white:#ffffff;
    --blue:#0a66f5;
    --purple:#4a0c98;
    --green:#0bb30f;
    --glass:rgba(232,220,236,0.8);
    --glass-line:rgba(255,255,255,0.85);
    --label-grey:#4a4a4a;
    --link-blue:#1f5aa6;
    --avatar:#1f1f1f;
  }
  *{margin:0;padding:0;box-sizing:border-box;}
  html,body{width:1200px;height:1000px;overflow:hidden;}
  body{background:var(--page-bg);font-family:"Roboto",Helvetica,Arial,sans-serif;position:relative;}
  .screen{
    position:absolute;left:328px;top:20px;width:340px;height:600px;
    transform:scale(1.6);transform-origin:0 0;overflow:hidden;color:var(--white);
    background:
      radial-gradient(ellipse 70% 18% at 55% 27%, rgba(240,170,235,0.9), rgba(240,170,235,0) 100%),
      radial-gradient(ellipse 80% 30% at 45% 65%, rgba(190,90,160,0.55), rgba(190,90,160,0) 100%),
      linear-gradient(180deg,#4a1c4e 0%,#8e4a8f 18%,#b46cb4 28%,#7c3a7e 45%,#5a1f5a 62%,#2a0a25 78%,#120410 100%);
  }
  .status-bar{position:absolute;top:4px;left:6px;right:6px;height:16px;font-size:11.5px;display:flex;align-items:center;justify-content:space-between;}
  .status-bar .time{position:absolute;left:50%;transform:translateX(-50%);font-weight:500;}
  .status-left,.status-right{display:flex;align-items:center;gap:4px;}
  .nav-title{position:absolute;top:32px;width:100%;text-align:center;font-size:21px;font-weight:500;}
  .nav-back{position:absolute;left:22px;top:38px;}
  .bar{position:absolute;left:10px;width:320px;height:46px;display:flex;align-items:center;justify-content:center;font-size:18px;}
  .bar .bar-icon{position:absolute;right:24px;top:12px;}
  .group-select{top:90px;background:var(--blue);}
  .recent-panel{position:absolute;left:10px;top:160px;width:320px;height:171px;background:var(--glass);border-top:1px solid var(--glass-line);}
  .recent-head{height:46px;display:flex;align-items:center;justify-content:space-between;padding:0 14px;border-bottom:1px solid var(--glass-line);}
  .recent-title{color:var(--label-grey);font-size:14.5px;letter-spacing:.2px;}
  .add-link{color:var(--link-blue);font-size:15px;display:flex;align-items:center;gap:7px;}
  .members{display:flex;justify-content:space-between;padding:10px 19px 0;}
  .member{width:78px;text-align:center;color:#333;font-size:14px;}
  .avatar{width:78px;height:78px;border-radius:50%;background:var(--avatar);border:2px solid var(--white);margin-bottom:5px;}
  .view-all{top:331px;background:var(--purple);}
  .create{top:401px;background:var(--green);}
  .tab-bar{position:absolute;left:0;top:505px;width:100%;display:flex;justify-content:space-between;padding:0 13px;}
  .tab{width:78px;text-align:center;font-size:12px;}
  .tab-icon{width:54px;height:54px;border-radius:50%;border:1.5px solid var(--white);margin:0 auto 7px;display:flex;align-items:center;justify-content:center;}
  .tab.active .tab-icon{background:var(--blue);border-color:var(--blue);}
  .tab-letter{font-size:24px;font-weight:300;}
</style>
</head>
<body>
<main class="screen">
  <div class="status-bar">
    <div class="status-left">
      <svg width="30" height="6" viewBox="0 0 30 6"><g fill="#fff"><circle cx="3" cy="3" r="2.6"/><circle cx="9" cy="3" r="2.6"/><circle cx="15" cy="3" r="2.6"/></g><g fill="none" stroke="#fff" stroke-width=".8"><circle cx="21" cy="3" r="2.3"/><circle cx="27" cy="3" r="2.3"/></g></svg>
      <span>NORA</span>
      <svg width="13" height="10" viewBox="0 0 13 10" fill="none" stroke="#fff" stroke-width="1.3"><path d="M1 3.5a8 8 0 0 1 11 0M3 5.7a5 5 0 0 1 7 0"/><circle cx="6.5" cy="8.3" r="1" fill="#fff" stroke="none"/></svg>
    </div>
    <span class="time">4:21 PM</span>
    <div class="status-right">
      <svg width="7" height="11" viewBox="0 0 7 11" fill="none" stroke="#fff" stroke-width="1"><path d="M1 3l5 5-2.5 2V1L6 3 1 8"/></svg>
      <span>100%</span>
      <svg width="24" height="11" viewBox="0 0 24 11"><rect x=".5" y=".5" width="21" height="10" rx="2" fill="none" stroke="#fff"/><rect x="2" y="2" width="18" height="7" fill="#fff"/><rect x="22" y="3.5" width="1.5" height="4" fill="#fff"/></svg>
    </div>
  </div>

  <svg class="nav-back" width="10" height="16" viewBox="0 0 10 16" fill="none" stroke="#fff" stroke-width="2"><path d="M8 2L2 8l6 6"/></svg>
  <h1 class="nav-title">My Vrenn</h1>

  <div class="bar group-select">Sloths
    <svg class="bar-icon" width="22" height="22" viewBox="0 0 22 22"><circle cx="11" cy="11" r="11" fill="#fff"/><path d="M6.5 9l4.5 4.5L15.5 9" fill="none" stroke="#0a66f5" stroke-width="2.4"/></svg>
  </div>

  <section class="recent-panel">
    <div class="recent-head">
      <span class="recent-title">RECENTLY ADDED</span>
      <span class="add-link">
        <svg width="20" height="20" viewBox="0 0 20 20"><circle cx="10" cy="10" r="10" fill="#1f5aa6"/><path d="M10 5v10M5 10h10" stroke="#fff" stroke-width="1.6"/></svg>Add</span>
    </div>
    <div class="members">
      <div class="member"><div class="avatar"></div>user1</div>
      <div class="member"><div class="avatar"></div>user1</div>
      <div class="member"><div class="avatar"></div>user3</div>
    </div>
  </section>

  <div class="bar view-all">View All
    <svg class="bar-icon" width="22" height="22" viewBox="0 0 22 22"><circle cx="11" cy="11" r="11" fill="#fff"/><path d="M9 6.5l4.5 4.5L9 15.5" fill="none" stroke="#4a0c98" stroke-width="2.4"/></svg>
  </div>

  <div class="bar create">Create a Vrenn</div>

  <nav class="tab-bar">
    <div class="tab"><div class="tab-icon">
      <svg width="30" height="28" viewBox="0 0 30 28" fill="none" stroke="#fff" stroke-width="1.5"><circle cx="11" cy="8" r="5"/><path d="M2 25c0-6 4-9 9-9s9 3 9 9z"/><circle cx="20" cy="12" r="4"/><path d="M16 25h12c0-5-3-8-8-8"/></svg>
    </div>Profile</div>
    <div class="tab active"><div class="tab-icon"><span class="tab-letter">v</span></div>My Vrenn</div>
    <div class="tab"><div class="tab-icon">
      <svg width="26" height="26" viewBox="0 0 26 26" fill="none" stroke="#fff" stroke-width="1.5"><path d="M14 3h9v9L12 23 3 14z"/><circle cx="18.5" cy="7.5" r="1.6"/></svg>
    </div>Tickets</div>
    <div class="tab"><div class="tab-icon">
      <svg width="30" height="30" viewBox="0 0 30 30" fill="none" stroke="#fff" stroke-width="1.4"><circle cx="15" cy="15" r="3.5"/><circle cx="15" cy="5" r="2.2"/><circle cx="15" cy="25" r="2.2"/><circle cx="5" cy="15" r="2.2"/><circle cx="25" cy="15" r="2.2"/><circle cx="8" cy="8" r="2.2"/><circle cx="22" cy="8" r="2.2"/><circle cx="8" cy="22" r="2.2"/><circle cx="22" cy="22" r="2.2"/></svg>
    </div>Events</div>
  </nav>
</main>
</body>
</html>
```